Business card for a plastic surgeon

i need a business card for a plastic surgeon. I have two adresses. The card should communicate safety, simmetry, beauty and with soft colors.
What i want in the card:
- my logo: Letters "R"and "B" (picture uploaded)
- my name: Renato Bastiani
- my registration: CRM 507 219
- my adresses and phone numbers (2):
- Av Dr Teixeira Lopes, 2710, sala 305 - Vila Olímpia | São Paulo/ SP - Phone: 11 4172-5036
- Al. Itapeva, 47, 3 andar - Alphaville | Barueri/ SP - Phone: 11 6350-2481

- my social network: site, facebook and instagram

Target Market(s)

people (95% girls and women) that want cosmetic procedures and plastic surgery

Industry/Entity Type

Business

Contact Information for Business Card

The card should communicate safety, simmetry, beauty and with soft colors.
Beige, brown, gray, rosy are some options. Color is free

Font styles to use
Serif

Requirements
Must have
• - my logo: Letters "R"and "B" (picture uploaded)
• - my name: Renato Bastiani
• - my registration: CRM 507 219
• - my adresses and phone numbers (2):
• - Av Dr Teixeira Lopes, 2710, sala 305 - Vila Olímpia | São Paulo/ SP - Phone: 11 4172-5036
• - Al. Itapeva, 47, 3 andar - Alphaville | Barueri/ SP - Phone: 11 6350-2481
• - my social network: site, facebook and instagram
Should not have
• other images (only my logo)

```html
<!DOCTYPE html>
<html lang="pt-BR">
<head>
<meta charset="utf-8">
<title>Renato Bastiani – Cartão de visita</title>
<link href="https://fonts.googleapis.com/css2?family=Pinyon+Script&family=Source+Sans+3:wght@300;400&display=swap" rel="stylesheet">
<style>
  :root {
    --backdrop: #1c1c1c;
    --paper: #ffffff;
    --taupe: #a58b74;
    --taupe-text: #9f8772;
    --ink: #262626;
    --on-taupe: #ffffff;
  }
  html, body {
    margin: 0;
    padding: 0;
    width: 1200px;
    height: 900px;
    overflow: hidden;
    background: var(--backdrop);
  }
  .canvas {
    position: relative;
    width: 1200px;
    height: 900px;
    font-family: "Source Sans 3", "Myriad Pro", Arial, sans-serif;
  }
  .card {
    position: absolute;
    top: 170px;
    width: 347px;
    height: 561px;
    box-sizing: border-box;
    text-align: center;
  }
  .card--front { left: 259px; background: var(--paper); color: var(--ink); }
  .card--back { left: 631px; background: var(--taupe); color: var(--on-taupe); }

  .monogram {
    position: absolute;
    left: 0;
    right: 0;
    margin: 0;
    font-weight: 300;
    font-size: 110px;
    line-height: 1;
    letter-spacing: 2px;
    transform: translateY(-50%);
  }
  .card--front .monogram { top: 140px; color: var(--taupe); }
  .card--back .monogram { top: 228px; color: var(--on-taupe); }

  .doctor-name {
    position: absolute;
    top: 262px;
    left: 0;
    right: 0;
    margin: 0;
    font-family: "Pinyon Script", "Times New Roman", serif;
    font-weight: 400;
    font-size: 38px;
    color: var(--taupe-text);
    line-height: 1;
  }
  .office {
    position: absolute;
    left: 0;
    right: 0;
    margin: 0;
  }
  .office--sp { top: 347px; }
  .office--barueri { top: 446px; }
  .office__address { margin: 0; font-size: 15.5px; line-height: 21px; }
  .office--barueri .office__address { font-size: 17.5px; line-height: 22px; }
  .office__phone { margin: 8px 0 0; font-size: 17px; line-height: 20px; }

  .registration {
    position: absolute;
    top: 356px;
    left: 0;
    right: 0;
    margin: 0;
    font-size: 17.5px;
  }
  .social {
    position: absolute;
    top: 484px;
    left: 0;
    right: 0;
    display: flex;
    justify-content: center;
    gap: 18px;
  }
  .social__badge {
    width: 26px;
    height: 26px;
    border-radius: 5px;
    background: var(--on-taupe);
  }
</style>
</head>
<body>
<main class="canvas">
  <section class="card card--front" aria-label="Frente do cartão">
    <div class="monogram">RB</div>
    <h1 class="doctor-name">Renato Bastiani</h1>
    <div class="office office--sp">
      <p class="office__address">Av Dr Teixeira Lopes, 2710, sala<br>305 - Vila Olímpia | São Paulo/ SP</p>
      <p class="office__phone">11 4172-5036</p>
    </div>
    <div class="office office--barueri">
      <p class="office__address">Al. Itapeva, 47, 3 andar - Alphaville<br>Barueri/ SP</p>
      <p class="office__phone">11 6350-2481</p>
    </div>
  </section>

  <section class="card card--back" aria-label="Verso do cartão">
    <div class="monogram">RB</div>
    <p class="registration">Reg No. CRM 507 219</p>
    <div class="social" aria-label="Redes sociais">
      <span class="social__badge"></span>
      <span class="social__badge"></span>
    </div>
  </section>
</main>
</body>
</html>
```